Building company buisness cards

We are looking for a sharp modern new look for our business cards.
We are a New Zealand based company that specialises in house and land packages.
We have attached a photo of the current logo and would like to see if it can be improved somehow if needed.
We are open to any colours but we have chosen green at this stage.
Feel free to change the font and make the logo smarter looking.
Play with the colours and see what looks best.

We want a card that looks so good know one will want to throw it away!

Target Market(s)

Home buyers

Industry/Entity Type

Building

Contact Information for Business Card

Dorian Keswick
0217392604
dkeswick@tidewellhomecraft.co.nz
tidewellhomecraft.co.nz

Font styles to use
Serif
Sans Serif

Colors

Designer to choose colors to be used in the design.

Requirements
Must have
• Logo and company name on one side, details on the other side
Nice to have
• Color codes for the original green are HEX #4a8028, RGB(74,128,40), CMYK(42,0,69,50)
• Round corners, Raised and/or spot UV

```html
<!DOCTYPE html>
<html lang="en">
<head>
<meta charset="utf-8">
<title>Tidewell Homecraft – Business Cards</title>
<link rel="stylesheet" href="https://fonts.googleapis.com/css2?family=Montserrat:wght@400;600;800&display=swap">
<style>
  :root {
    --brand-green: #4a8028;
    --stripe-grey: #bdbdc2;
    --card-white: #ffffff;
    --ink: #333333;
    --backdrop: #2b2b2b;
  }
  * { margin: 0; padding: 0; box-sizing: border-box; }
  html, body { width: 1200px; height: 897px; overflow: hidden; background: var(--backdrop); }
  body { position: relative; font-family: "Montserrat", sans-serif; }

  .card {
    position: absolute;
    left: 303px;
    width: 594px;
    height: 338px;
    border-radius: 24px;
    overflow: hidden;
  }
  .card--front { top: 92px; background: var(--card-white); }
  .card--back { top: 470px; background: var(--brand-green); }

  .front-swoosh { position: absolute; inset: 0; width: 100%; height: 100%; }

  .wordmark {
    position: absolute;
    font-weight: 800;
    letter-spacing: -0.5px;
    line-height: 1;
    text-align: center;
  }
  .wordmark span { display: block; }
  .wordmark--front { left: 24px; top: 86px; width: 262px; color: var(--brand-green); }
  .wordmark--front .line-1 { font-size: 27px; }
  .wordmark--front .line-2 { font-size: 32px; margin-top: 4px; }
  .wordmark--back { left: 0; top: 154px; width: 100%; color: var(--card-white); }
  .wordmark--back .line-1 { font-size: 42px; }
  .wordmark--back .line-2 { font-size: 51px; margin-top: 4px; }

  .holder { position: absolute; right: 31px; top: 28px; text-align: right; }
  .holder-name { font-size: 22px; font-weight: 600; color: var(--brand-green); line-height: 1.1; }
  .holder-role { font-size: 15.5px; font-weight: 400; color: var(--ink); margin-top: 2px; }

  .contact-list {
    position: absolute;
    right: 28px;
    top: 250px;
    list-style: none;
    color: var(--card-white);
    font-size: 14.5px;
    font-weight: 400;
  }
  .contact-item { display: flex; justify-content: flex-end; align-items: center; height: 18.5px; }
  .contact-icon { width: 11px; height: 11px; margin-left: 8px; flex: none; }
</style>
</head>
<body>
  <section class="card card--front" aria-label="Business card front">
    <svg class="front-swoosh" viewBox="0 0 594 338" preserveAspectRatio="none" aria-hidden="true">
      <path d="M0,338 L0,318 C120,214 330,150 594,152 L594,338 Z" fill="var(--brand-green)"/>
      <path d="M20,338 C140,236 345,160 594,153 L594,338 Z" fill="var(--stripe-grey)"/>
      <path d="M40,338 C165,242 370,168 594,156 L594,338 Z" fill="var(--brand-green)"/>
    </svg>

    <div class="wordmark wordmark--front">
      <span class="line-1">tidewell</span>
      <span class="line-2">homecraft.</span>
    </div>

    <div class="holder">
      <p class="holder-name">Dorian Keswick</p>
      <p class="holder-role">Founder</p>
    </div>

    <ul class="contact-list">
      <li class="contact-item">0217392604
        <svg class="contact-icon" viewBox="0 0 12 12" aria-hidden="true"><path d="M3 1 L5 3.5 L4 5 C5 7 6 8 7.5 8.5 L9 7.5 L11 9.5 L9.5 11 C5.5 10.5 1.5 6.5 1 2.5 Z" fill="none" stroke="#fff" stroke-width="1.2" stroke-linejoin="round"/></svg>
      </li>
      <li class="contact-item">dkeswick@tidewellhomecraft.co.nz
        <svg class="contact-icon" viewBox="0 0 12 12" aria-hidden="true"><rect x="1" y="2.5" width="10" height="7" fill="none" stroke="#fff" stroke-width="1.2"/><path d="M1 2.5 L6 6.5 L11 2.5" fill="none" stroke="#fff" stroke-width="1.2"/></svg>
      </li>
      <li class="contact-item">tidewellhomecraft.co.nz
        <svg class="contact-icon" viewBox="0 0 12 12" aria-hidden="true"><circle cx="6" cy="6" r="5" fill="none" stroke="#fff" stroke-width="1.1"/><ellipse cx="6" cy="6" rx="2.2" ry="5" fill="none" stroke="#fff" stroke-width="1"/><path d="M1 6 H11 M2 3.5 H10 M2 8.5 H10" stroke="#fff" stroke-width="1"/></svg>
      </li>
    </ul>
  </section>

  <section class="card card--back" aria-label="Business card back">
    <div class="wordmark wordmark--back">
      <span class="line-1">tidewell</span>
      <span class="line-2">homecraft.</span>
    </div>
  </section>
</body>
</html>
```